Make a medical leaflet for my patients undergoing ankle blocks

I have a very boring text only leaflet I would like to turn into a professional appealing medical leaflet to give to my patients. I would like to get this onto two pages of a4 if possible and its intended for electronic distribution mainly.
This will be for patients so it must be professional.
It must also contain a copyright logo on it and my name near the start (Dr Tobias Renner) so my colleagues can't use it easily.
Target Market(s)
Patients undergoing surgery
Industry/Entity Type
Medical
Other font styles liked:
- no idea, you tell me
Requirements
Must have
- the information contained on the attachment
- look professional
- a copyright on it
Nice to have
- the fernbrook clinic logo
Should not have
- Any spelling, grammatical or linguistic errors
- Any font less than size 12

```html
<!DOCTYPE html>
<html lang="en">
<head>
<meta charset="utf-8">
<title>Ankle Block – Patient Information</title>
<link rel="stylesheet" href="https://fonts.googleapis.com/css2?family=Lato:ital,wght@0,300;0,400;0,700;0,900;1,300;1,400&display=swap">
<style>
  :root {
    --page-blue: #1a90c7;
    --ink-white: #ffffff;
  }
  * { box-sizing: border-box; margin: 0; padding: 0; }
  html, body {
    width: 848px; height: 1200px; overflow: hidden;
    background: var(--page-blue);
  }
  .leaflet-page {
    position: relative; width: 848px; height: 1200px;
    background: var(--page-blue); color: var(--ink-white);
    font-family: "Lato", sans-serif; font-weight: 300;
    font-size: 17.6px; line-height: 22.8px;
  }
  .column { position: absolute; top: 37px; width: 374px; }
  .column--left { left: 41px; }
  .column--right { left: 436px; }

  .risk-heading {
    display: flex; font-style: italic; font-weight: 400;
  }
  .risk-heading .num { width: 25px; flex: none; }

  .body-text { margin-top: 16px; }
  .body-text--tight { margin-top: 8px; }

  .bullet-list { list-style: none; margin-top: 12px; }
  .bullet-list li {
    position: relative; padding-left: 25px; margin-bottom: 11px;
  }
  .bullet-list li::before {
    content: ""; position: absolute; left: 5px; top: 9px;
    width: 5px; height: 5px; border-radius: 50%; background: var(--ink-white);
  }
  .bullet-list--options li { font-style: italic; font-weight: 400; margin-bottom: 12px; }

  .section-title {
    font-weight: 900; font-size: 27px; line-height: 30px;
    letter-spacing: 0.16em; text-transform: uppercase;
    margin-top: 24px;
  }
  .sub-title {
    font-weight: 400; font-size: 17.6px; line-height: 22.8px;
    margin-top: 10px;
  }
  .closing-note {
    font-style: italic; font-size: 15.2px; line-height: 22px; margin-top: 12px;
  }
</style>
</head>
<body>
<main class="leaflet-page">
  <section class="column column--left">
    <p class="risk-heading"><span class="num">2.</span><span>Pain during operation - If you choose to have wide awake surgery or surgery under sedation</span></p>
    <p class="body-text">The surgery will stop and I will discuss three options with you</p>
    <ul class="bullet-list bullet-list--options">
      <li>more numbing liquid to be injected by the surgeon</li>
      <li>more sedation / painkiller</li>
      <li>having a general anaesthetic</li>
    </ul>
    <p class="body-text body-text--tight">If you decide to undergo surgery awake or sedated, there is a risk you will need to have a general anaesthetic if you feel pain. This is why the starvation instructions of awake surgery and general anaesthesia are the same.</p>

    <h2 class="section-title">How is it done</h2>
    <h3 class="sub-title">If you choose awake surgery or surgery with sedation:</h3>
    <ul class="bullet-list">
      <li>Numbing liquid is injected around the nerves which supply your foot.</li>
      <li>The ankle block takes 5 - 10 minutes to perform and requires 4 - 5 injections</li>
      <li>Approximately 10 - 20 minutes to make your foot numb to pain.</li>
      <li>I will check the ankle block is working before we start surgery using cold spray</li>
      <li>Sensations of touch, pressure, vibration and movement will still be felt</li>
      <li>I will use a screen so you can’t see the surgery (unless you would like to see)</li>
      <li>Some patients bring headphones to block out the noise of the operation.</li>
    </ul>

    <h3 class="sub-title">If you choose a General anaesthetic:</h3>
    <ul class="bullet-list">
      <li>I will perform the ankle block after I start the general anaesthetic.</li>
      <li>You should wake up from your surgery with a comfortable and numb foot/feet.</li>
      <li>If you wake in pain, we can repeat the ankle block or provide traditional painkillers.</li>
    </ul>
  </section>

  <section class="column column--right">
    <p>Whatever you choose, there will be a cannula placed in your hand and heart and oxygen monitoring throughout.</p>

    <h2 class="section-title" style="margin-top:14px">After surgery</h2>
    <p class="body-text body-text--tight">You will go to the recovery area and then onto the ward when you are ready. It will be difficult to walk while the block is working so physiotherapists will help you first walk. If you need crutches they will teach you how to use them.</p>
    <p class="body-text">Your foot will be numb and so you will not feel where your foot is in relation to nearby objects. As a result, it is easy to knock your foot. Please take extra care while your foot is still numb.</p>
    <p class="body-text">As the block wears off, the foot may feel slightly painful, tingly or hot. At this point you should take your painkillers I have prescribed. Depending on your medical history you will have up to three painkillers. I would suggest to start with all three. You will also have an anti - sickness prescribed if one of the painkillers (typically codeine or morphine) makes you feel sick.</p>
    <p class="body-text">Occasionally (1 - 2%), pain when the block wears off will be severe. In this case contact your surgeon’s secretary. We can use stronger pain medication, but there will be charge in writing and getting the private prescription to you (please see my terms of business) via courier.</p>

    <h2 class="section-title">The alternative</h2>
    <p class="body-text body-text--tight">If you do not have an ankle block your surgery can still proceed.</p>
    <ul class="bullet-list">
      <li>Post operative pain can be managed with traditional painkillers.</li>
      <li>However, you are more likely to need an overnight stay or feel sick after the anaesthetic.</li>
    </ul>
    <p class="body-text body-text--tight">If you have any further questions about an ankle block I will see you the day of your surgery.</p>
    <p class="closing-note">Alternatively, you can request the following optional services (as mentioned in my terms of business).</p>
  </section>
</main>
</body>
</html>
```